inspirational business card

I want to use the Vector on Pixmarra.com (number 61827405) and I will purchase the vector to send it to the designer once the general concept is approved. You can download it for free for a one time use on providing a design for this request.
Within the vector, insert:
Denise Halvorsen
Guidance and Cooperative

I prefer a vertical card but do not require vertical.

Contact info:

Denise Halvorsen, J.D.
Collaborative Lawyer
Certified Divorce Coach
Mediation Coach
PHONE 641/382-4076
EMAIL: dhrt@quelvo.net

Website: Guidanceandcooperative.com
Settlementcourse.com

I like greens, blue and grey. I do not want black font, and would like the font to be legible without needing perfect reading vision (no super small font).
I would like the overall theme to convey growth and nurturance.
I like the vector I selected because of the growth and light portrayed.
Not too frilly or too bold. I would like to to appeal to both sexes.

Target Market(s)

Generally professional women 35-60

Industry/Entity Type

Attorney

Font styles to use
Serif
Sans Serif

Colors
acd136
cadf82
fbf289
9d9d9d

Requirements
Must have
• My project does not need to have my photo but you could use it if you want
Nice to have
• Vertical
• I like rounded edges on the cards
Should not have
• I do not like my name appearing two times in close proximity. I'm not a flowery person.

```html
<!DOCTYPE html>
<html lang="en">
<head>
<meta charset="utf-8">
<title>Denise Halvorsen – Business Card</title>
<link rel="stylesheet" href="https://fonts.googleapis.com/css2?family=Cinzel:wght@400&family=Tinos&family=Roboto:wght@400&display=swap">
<style>
  :root {
    --lime: #c6dd4a;
    --leaf: #9dc23a;
    --forest: #5f9638;
    --deep: #4f8a31;
    --grey: #9d9d9d;
    --ink-grey: #6d6d6d;
    --pale: #e9ede4;
    --white: #ffffff;
    --stage: #e4e6e2;
  }
  * { margin: 0; padding: 0; box-sizing: border-box; }
  html, body { width: 1200px; height: 900px; overflow: hidden; background: var(--stage); }
  .canvas { position: relative; width: 1200px; height: 900px; }

  .card {
    position: absolute;
    width: 700px; height: 400px;
    border-radius: 28px;
    overflow: hidden;
    box-shadow: 0 6px 18px rgba(0,0,0,0.12);
  }
  .card svg.card-art { position: absolute; inset: 0; }

  /* Back card */
  .card-back {
    left: 450px; top: 45px;
    background: linear-gradient(200deg, var(--lime) 0%, var(--leaf) 45%, var(--forest) 100%);
  }
  .back-brand {
    position: absolute; left: 0; width: 560px; top: 222px;
    text-align: center; color: var(--pale);
  }
  .back-brand .brand-name {
    font-family: "Cinzel", serif; font-size: 46px; letter-spacing: 1px; line-height: 1;
  }
  .back-brand .brand-line {
    font-family: "Cinzel", serif; font-size: 15px; letter-spacing: 2px; margin-top: 8px;
  }

  /* Front card */
  .card-front { left: 55px; top: 470px; background: var(--white); }
  .front-identity {
    position: absolute; right: 40px; top: 38px; text-align: right;
    font-family: "Tinos", serif;
  }
  .front-identity .person-name { font-size: 34px; color: var(--ink-grey); line-height: 1.1; }
  .front-identity .role { font-size: 22px; color: var(--forest); line-height: 1.3; }
  .front-contacts {
    position: absolute; right: 70px; top: 262px; text-align: right;
    font-family: "Roboto", sans-serif; font-size: 19px; color: var(--white);
    line-height: 30px;
  }
</style>
</head>
<body>
<main class="canvas">

  <section class="card card-back" aria-label="Card back">
    <svg class="card-art" width="700" height="400" viewBox="0 0 700 400">
      <defs>
        <radialGradient id="glow" cx="0.5" cy="0.5" r="0.5">
          <stop offset="0" stop-color="#ffffff" stop-opacity="0.28"/>
          <stop offset="1" stop-color="#ffffff" stop-opacity="0"/>
        </radialGradient>
      </defs>
      <ellipse cx="610" cy="230" rx="150" ry="190" fill="url(#glow)" role="img" aria-label="Faint tree decoration area"/>
      <circle cx="440" cy="118" r="88" fill="none" stroke="var(--white)" stroke-width="8"/>
      <circle cx="440" cy="118" r="76" fill="var(--white)" fill-opacity="0.22" role="img" aria-label="Brand symbol area"/>
    </svg>
    <div class="back-brand">
      <div class="brand-name">DENISE HALVORSEN</div>
      <div class="brand-line">GUIDANCE AND COOPERATIVE</div>
    </div>
  </section>

  <section class="card card-front" aria-label="Card front">
    <svg class="card-art" width="700" height="400" viewBox="0 0 700 400">
      <defs>
        <linearGradient id="sweep" x1="0" y1="0" x2="1" y2="0.4">
          <stop offset="0" stop-color="var(--lime)"/>
          <stop offset="0.55" stop-color="var(--leaf)"/>
          <stop offset="1" stop-color="var(--deep)"/>
        </linearGradient>
      </defs>
      <path d="M0,145 C60,195 160,215 320,222" fill="none" stroke="var(--grey)" stroke-width="12"/>
      <path d="M0,175 C150,235 380,225 700,230 L700,400 L0,400 Z" fill="url(#sweep)"/>
      <path d="M30,200 C200,250 420,225 600,240" fill="none" stroke="var(--white)" stroke-width="8" stroke-linecap="round"/>
      <circle cx="165" cy="112" r="90" fill="none" stroke="var(--forest)" stroke-width="10"/>
      <circle cx="165" cy="112" r="76" fill="var(--leaf)" fill-opacity="0.35" role="img" aria-label="Brand symbol area"/>

      <g class="contact-icons" fill="var(--white)">
        <circle cx="650" cy="277" r="12"/>
        <circle cx="650" cy="307" r="12"/>
        <circle cx="650" cy="337" r="12"/>
        <circle cx="650" cy="367" r="12"/>
      </g>
      <g fill="none" stroke="var(--forest)" stroke-width="2">
        <path d="M644,280 q6,-9 12,0 M646,279 h8 v4 h-8 z"/>
        <rect x="643" y="302" width="14" height="10"/>
        <path d="M643,302 l7,6 l7,-6"/>
        <circle cx="650" cy="337" r="7"/>
        <path d="M643,337 h14 M650,330 v14"/>
        <circle cx="650" cy="367" r="7"/>
        <path d="M643,367 h14 M650,360 v14"/>
      </g>
    </svg>
    <div class="front-identity">
      <div class="person-name">Denise Halvorsen, J.D</div>
      <div class="role">Collaborative Lawyer</div>
      <div class="role">Certified Divorce Coach</div>
      <div class="role">Mediation Coach</div>
    </div>
    <div class="front-contacts">
      <div>641/382-4076</div>
      <div>dhrt@quelvo.net</div>
      <div>guidanceandcooperative.com</div>
      <div>settlementcourse.com</div>
    </div>
  </section>

</main>
</body>
</html>
```